Business Card Design Project used as hotel key

I need a project to be printed on PVC card and used by our customers as room key.

The design and the color are up to you. My idea would be to include the logo (colour can also be changed) on the front side and our Internet address on the back (http://www.valmirenza.ch, info@valmirenza.ch).

Target Market(s)

Hôtel customers

Industry/Entity Type

Hotel

Requirements
Must have
• I have attached below the template of the front and back of the card. The logo on the back shown on the template below the magnetic stripe should not be used.

Must have:

1. Follow the template size (shown in the template):

Full Bleed Size:
3.55" x 2.3"
90.17mm x 58.42mm
1065 x 690 pixels

Trim Size:
3.375" x 2.125"
85.77mm x 54.02mm
1013 x 638 pixels

A bleed is the outer area of your artwork that falls on the outside of the trim line. It is important that you do not have any important information in the bleed area as ¼ “ will be cut off on all sides. Cards with a “framed border” are not recommended due to variances in die cutting.

2. Make sure you leave the area between the magstripe markers on the template blank.

3. There need to be an arrow on the front side (on the left), pointing the left side

4. Color: Full color both sides, color process CMYK. 300 DPI at 100% of the final print size

```html
<!DOCTYPE html>
<html lang="en">
<head>
<meta charset="utf-8">
<title>Hôtel Valmirenza – Room Key Card</title>
<link rel="stylesheet" href="https://fonts.googleapis.com/css2?family=Arimo:wght@400&family=Oswald:wght@600&display=swap">
<style>
  :root {
    --paper: #ffffff;
    --bark: #5b4840;
    --bark-deep: #3f2b22;
    --leaf-light: #a48d80;
    --leaf-dark: #3e261b;
    --stripe: #000000;
    --ink: #ffffff;
    --label: #111111;
    --bleed: #e0344a;
    --trim: #4caf50;
    --safe: #3f6fc4;
  }
  * { box-sizing: border-box; margin: 0; padding: 0; }
  html, body { width: 1200px; height: 848px; overflow: hidden; background: var(--paper); }
  body { position: relative; font-family: "Arimo", Arial, sans-serif; }

  .side-label { position: absolute; top: 333px; font-size: 15px; color: var(--label); width: 120px; text-align: center; }
  .side-label--front { left: 112px; }
  .side-label--back { left: 372px; }

  .card { position: absolute; overflow: hidden; background: var(--bark); }
  .card--flat { width: 237px; height: 368px; top: 364px; border: 1px solid var(--bleed); }
  .card--flat-front { left: 60px; }
  .card--flat-back { left: 320px; }
  .card--mock { width: 221px; height: 349px; top: 118px; border-radius: 18px; }
  .card--mock-front { left: 635px; }
  .card--mock-back { left: 895px; }

  .ornament { position: absolute; border-radius: 45%; }
  .ornament--upper { right: -10%; top: 0; width: 80%; height: 55%;
    background: radial-gradient(ellipse at 55% 40%, rgba(164,141,128,.55), rgba(164,141,128,0) 70%); }
  .ornament--lower { left: -8%; top: 45%; width: 60%; height: 35%;
    background: radial-gradient(ellipse at 40% 50%, rgba(62,38,27,.7), rgba(62,38,27,0) 70%); }
  .card--flat-back .ornament--lower, .card--mock-back .ornament--lower { left: auto; right: -8%; top: 50%; }

  .guide { position: absolute; pointer-events: none; }
  .guide--trim { inset: 7px 6px 7px 7px; border: 1px solid var(--trim); border-radius: 12px; }
  .guide--safe { left: 22px; right: 20px; top: 22px; bottom: 24px; border: 1px solid var(--safe); }

  .magstripe { position: absolute; top: 0; bottom: 0; background: var(--stripe); }
  .card--flat-back .magstripe { left: 25px; width: 53px; bottom: 4px; }
  .card--mock-back .magstripe { left: 15px; width: 53px; }

  .hotel-name { position: absolute; font-family: "Oswald", "Arial Narrow", sans-serif; font-weight: 600;
    color: var(--ink); letter-spacing: .5px; white-space: nowrap; text-transform: uppercase; }
  .card--flat-front .hotel-name { left: 36px; top: 234px; font-size: 22px; }
  .card--mock-front .hotel-name { left: 27px; top: 233px; font-size: 21px; }

  .arrow { position: absolute; width: 0; height: 0;
    border-left: 34px solid transparent; border-right: 34px solid transparent; border-top: 19px solid var(--leaf-light); }
  .card--flat-front .arrow { left: 85px; top: 321px; }
  .card--mock-front .arrow { left: 74px; top: 312px; }

  .contact { position: absolute; writing-mode: vertical-rl; transform: rotate(180deg);
    color: var(--ink); white-space: nowrap; letter-spacing: .3px; }
  .card--flat-back .contact { font-size: 17px; bottom: 97px; }
  .card--flat-back .contact--web { left: 107px; }
  .card--flat-back .contact--mail { left: 154px; }
  .card--mock-back .contact { font-size: 15.5px; bottom: 87px; }
  .card--mock-back .contact--web { left: 99px; }
  .card--mock-back .contact--mail { left: 145px; }

  .icon { position: absolute; border-radius: 50%; background: var(--leaf-dark); display: flex; align-items: center; justify-content: center; }
  .card--flat-back .icon { width: 40px; height: 40px; top: 279px; }
  .card--flat-back .icon--web { left: 97px; }
  .card--flat-back .icon--mail { left: 144px; }
  .card--mock-back .icon { width: 36px; height: 36px; top: 273px; }
  .card--mock-back .icon--web { left: 90px; }
  .card--mock-back .icon--mail { left: 135px; }
  .icon svg { width: 55%; height: 55%; }

  .legend { position: absolute; left: 95px; font-size: 14px; color: var(--label); }
  .legend::after { content: ""; position: absolute; left: 91px; top: 9px; width: 120px; height: 1px; }
  .legend--bleed { top: 777px; }
  .legend--bleed::after { background: var(--bleed); }
  .legend--trim { top: 797px; }
  .legend--trim::after { background: var(--trim); }
</style>
</head>
<body>
  <div class="side-label side-label--front">front</div>
  <div class="side-label side-label--back">back</div>

  <!-- Print layout: front -->
  <div class="card card--flat card--flat-front">
    <div class="ornament ornament--upper" role="img" aria-label="Pale taupe floral swirl ornament"></div>
    <div class="ornament ornament--lower" role="img" aria-label="Dark brown floral swirl ornament"></div>
    <div class="hotel-name">Hôtel Valmirenza</div>
    <div class="arrow"></div>
    <div class="guide guide--trim"></div>
    <div class="guide guide--safe"></div>
  </div>

  <!-- Print layout: back -->
  <div class="card card--flat card--flat-back">
    <div class="ornament ornament--upper" role="img" aria-label="Pale taupe floral swirl ornament"></div>
    <div class="ornament ornament--lower" role="img" aria-label="Dark brown floral swirl ornament"></div>
    <div class="magstripe"></div>
    <div class="contact contact--web">http://www.valmirenza.ch</div>
    <div class="contact contact--mail">info@valmirenza.ch</div>
    <div class="icon icon--web">
      <svg viewBox="0 0 24 24" fill="none" stroke="#fff" stroke-width="1.8"><circle cx="12" cy="12" r="10"/><ellipse cx="12" cy="12" rx="4.5" ry="10"/><path d="M2 12h20M4 6.5h16M4 17.5h16"/></svg>
    </div>
    <div class="icon icon--mail">
      <svg viewBox="0 0 24 24" fill="none" stroke="#fff" stroke-width="1.8"><rect x="5" y="2" width="14" height="20"/><path d="M5 2l14 20M19 2L5 22"/></svg>
    </div>
    <div class="guide guide--trim"></div>
    <div class="guide guide--safe"></div>
  </div>

  <!-- Finished card: front -->
  <div class="card card--mock card--mock-front">
    <div class="ornament ornament--upper" role="img" aria-label="Pale taupe floral swirl ornament"></div>
    <div class="ornament ornament--lower" role="img" aria-label="Dark brown floral swirl ornament"></div>
    <div class="hotel-name">Hôtel Valmirenza</div>
    <div class="arrow"></div>
  </div>

  <!-- Finished card: back -->
  <div class="card card--mock card--mock-back">
    <div class="ornament ornament--upper" role="img" aria-label="Pale taupe floral swirl ornament"></div>
    <div class="ornament ornament--lower" role="img" aria-label="Dark brown floral swirl ornament"></div>
    <div class="magstripe"></div>
    <div class="contact contact--web">http://www.valmirenza.ch</div>
    <div class="contact contact--mail">info@valmirenza.ch</div>
    <div class="icon icon--web">
      <svg viewBox="0 0 24 24" fill="none" stroke="#fff" stroke-width="1.8"><circle cx="12" cy="12" r="10"/><ellipse cx="12" cy="12" rx="4.5" ry="10"/><path d="M2 12h20M4 6.5h16M4 17.5h16"/></svg>
    </div>
    <div class="icon icon--mail">
      <svg viewBox="0 0 24 24" fill="none" stroke="#fff" stroke-width="1.8"><rect x="5" y="2" width="14" height="20"/><path d="M5 2l14 20M19 2L5 22"/></svg>
    </div>
  </div>

  <div class="legend legend--bleed">Bleed Line</div>
  <div class="legend legend--trim">Trim Line</div>
</body>
</html>
```